Meadowlark Lane Yoga Facebook Design

"Practice Radiant Movement"

Foundational and sustainable yoga practice to cultivate growth through a variety of anatomy- informed movement patterns. Develop an informative and inspirational connection with the mind, body and spirit, through smart and integrated movement.

-I need a design that is happy and cheerful and attracts children and adults alike. I teach vinyassa based yoga that is sustainable and smart, kid yoga, and chair yoga.

-A movement practic rooted in foundation, core, and expression

- Accessible yoga for a sustained practice. A guided movement practice where one gains information and knowledge of oneself through a mind/body connection. For one feel good physically with a new awareness of their internal radiance that exists in all beings. Physical rejuvenation egnites a light and increases energy to flow through the physical body, which ultimately tranlates into works of kindness for others and out in the world.

Nora Whitfield
Yoga Instructor
MD, Pediatrician
RYT-200
RCYT
Certified yoga teacher for adults and children

Full description:
What is the positioning or mission statement of your company? to guide individuals in a yoga-based safe and sustainable movement practice applicable to all ages and body types. Currently my focus is working with children in daycare and school settings, but my goal is to expand into private yoga practice for adults, and potentially as part of rented space in studios. I hope to find a way to work with children AND adults (so would love for logo to be appealing to both), but current focus is with children based on need and demand in the community. yoga for children also compliments my backround as a pediatrician/neonatologist, and I greatly miss interacting with children. I also want to emphasize a yoga/movement practice that is focused more on what one feels internally through movement. NOT what one looks like asthetically. I believe in removing all mirrors from yoga/movement practice. It should be an experience of movement/poses/yoga through appropriate cueing and education. It is not about the details of how far the knee should bend, or how high the leg should be. Focusing on foudation first, core, then core engagement and ultimately expression of poses/movements. A focus on strength, stability and mobility, not just flexibility, which is the common perception/association with yoga. I also want individuals to learn to be an advocate of their own health. Through guidance, I hope for individuals to connect with their body so they know themselves so well to be able to advocate for themselves in the modern healthcare world. This internal experience and connection is so essential in a world where modern medicine has become a business and it is all about making a dollar. the connection with patients is lost, and individuals need to learn to empower themselves and through their new found voice to be able to articulate what is wrong.
Does your company have a tagline or slogan that should be included with the logo? "Practice Radiant Movement"
What do you hope your company can be known for? Accessible yoga for a sustained practice. A guided movement practice where one gains information and knowledge of oneself through a mind/body connection. For one feel good physically with a new awareness of their internal radiance that exists in all beings. Physical rejuvenation egnites a light and increases energy to flow through the physical body, which ultimately tranlates into works of kindness for others and out in the world.
What color palettes might you prefer? why? love the colors currently chosen
Where will the logo be primarily used? initially business cards, but hopefully future websites, t-shirts, and potentially local magazine adds. Also starting with a small couple of banners for community events in the area. I currently practice as a nomad out of my car :)
Are there any elements you would prefer to see in the logo? Movement. A modern depiction of a human body/figure practicing movement. Hoping to avoid a stereotypical yoga pose per say, just because I want to people to think of it more of a movement practice with yoga roots. Modern yoga. There are elements of breathing and connecting with oneself through the flow of breath and movement, but I do not focus on the meditative/cerebral aspect of the yoga practice. What I teach is almost reaching a meditative state through movement. I personally don't practice, nor resonate with just seated meditation. just not my thing :)
In your opinion, what defines a well-designed logo? curiosity. enough info for individuals to think they know what it means, but want to know more. invokes curiosity, but not too abstract. Reproducible. not too complicated. I want also to invoke a community feel, so a design that appeals to all people within a community.
What is your preference in reference to icons, typography, spokespeople (characters), etc.? modern design. I love the idea of a logo for my purposes, to invoke a sense of movement from within. So not too static.
What words or icons must be included in the logo? movement with yoga roots.
What logos do you like and why? A representation, but not exact. I think some ambiguity is intriguing for others, and also memorable. I want it to be an artistic representation of movement/yoga
What logos do you dislike and why? too busy, too loud.
In your opinion, what is the primary purpose for a logo? association
Who is the primary target audience? (who is most likely to use your services/product?) Children and their parents, but ultimately to expand into teaching adults. I even have aspirations of prenatal and post-natal yoga. Potentially incorporating infants.
Who currently uses your product the most? n/a (working in schools/daycare currently. It is currently all volunteer)
Are you pleased with the range of people your company serves? n/a
Are you looking to expand, modify, or completely change your target audience? or will it remain the same? yes! expand into an adult audience.
How do you plan to focus on your target audience? currently by working through schools and daycares. hopefully ultimately through after school care programs and then offering kid yoga in an existing yoga studio (working on this with Q studio in Ridgeland, currently)
What are your main forms of advertising? word of mouth, schools, daycares. Happy kids talking to their parents about the yoga class they took and happy teachers :)
How do most customers find out about your company?
Which gender are you targeting? All genders! However, with kid yoga, often the maternal individual in the child's life is more involved with decision making as far as extracurricular activities

Target Market(s)

Adults, children and families interested in movement, wellness and fun

Font styles to use
Sans Serif

Requirements
Must have
• ***I meant to emphasize the that "S" figure in my logo is SOOO iimportant to me. My daughter designed it. please highlight the "S" figure if possible******
My logo and the phrase "practice radiant movement"
Same colors as my logo
Feel like movement and fun.
Attracts children and families
Incorporate pieces of my description somehow
Nice to have
• different yoga poses or figures in movement
abstract design
attacts all body types and genders
inclusive

Industry is yoga, movement, wellness
Should not have
• no darkness
want happy and vibrant, inviting

```html
<!DOCTYPE html>
<html lang="en">
<head>
<meta charset="utf-8">
<title>Meadowlark Lane Yoga – Nora Whitfield, Yoga Instructor</title>
<link rel="stylesheet" href="https://fonts.googleapis.com/css2?family=Montserrat:wght@600;700;800;900&display=swap">
<style>
  :root {
    --paper: #ffffff;
    --leaf-green: #3aa53a;
    --lagoon: #5ec7ca;
    --sun-yellow: #f8d94a;
    --ink: #1f1f1f;
    --rule: #3a3a3a;
    --studio-wall: #eef1f3;
    --curtain-blue: #6aa3c8;
    --shirt-teal: #3fb4bd;
    --shirt-yellow: #f3d36a;
    --skin-warm: #e6cdb8;
    --mat-violet: #b07ac8;
  }
  * { margin: 0; padding: 0; box-sizing: border-box; }
  html, body {
    width: 1200px;
    height: 527px;
    overflow: hidden;
    background: var(--paper);
  }
  .banner {
    position: relative;
    width: 1200px;
    height: 527px;
    overflow: hidden;
    background: var(--paper);
    font-family: "Montserrat", Arial, sans-serif;
    color: var(--ink);
  }
  .banner__art {
    position: absolute;
    inset: 0;
    width: 1200px;
    height: 527px;
  }

  /* Brand block */
  .brand {
    position: absolute;
    top: 16px;
    left: 880px;
    width: 300px;
    display: flex;
    flex-direction: column;
    align-items: center;
    gap: 8px;
  }
  .brand__dot {
    width: 56px;
    height: 56px;
    border-radius: 50%;
    background: var(--sun-yellow);
  }
  .brand__name {
    font-weight: 700;
    font-size: 20px;
    color: var(--lagoon);
    text-align: center;
    line-height: 1.15;
    width: 200px;
  }
  .brand__tagline {
    font-weight: 700;
    font-size: 11px;
    letter-spacing: 1.2px;
    text-transform: uppercase;
    color: var(--lagoon);
  }

  /* Instructor block */
  .instructor {
    position: absolute;
    top: 186px;
    left: 850px;
    width: 330px;
    text-align: center;
  }
  .instructor__name {
    font-weight: 900;
    font-size: 41px;
    line-height: 1.02;
    letter-spacing: 1px;
    color: var(--leaf-green);
    text-transform: uppercase;
  }
  .instructor__role {
    margin-top: 4px;
    font-weight: 800;
    font-size: 28px;
    color: var(--ink);
  }
  .credentials {
    margin: 26px auto 0;
    width: 290px;
    border-top: 2px solid var(--rule);
    border-bottom: 2px solid var(--rule);
    padding: 8px 0 7px;
    font-weight: 600;
    font-size: 21px;
    letter-spacing: 1.5px;
    line-height: 1.4;
    text-transform: uppercase;
  }
  .instructor__note {
    margin-top: 22px;
    font-weight: 700;
    font-size: 16px;
    line-height: 1.3;
  }

  /* Contact list */
  .contact {
    position: absolute;
    left: 24px;
    top: 414px;
    list-style: none;
    display: flex;
    flex-direction: column;
    gap: 20px;
  }
  .contact__item {
    display: flex;
    align-items: center;
    gap: 10px;
    font-weight: 600;
    font-size: 24px;
    color: var(--ink);
  }
  .contact__icon {
    width: 26px;
    height: 26px;
    flex: none;
  }
</style>
</head>
<body>
<main class="banner">
  <svg class="banner__art" viewBox="0 0 1200 527">
    <defs>
      <linearGradient id="class-photo-tone" x1="0" y1="0" x2="1" y2="0.35">
        <stop offset="0" stop-color="var(--shirt-yellow)"/>
        <stop offset="0.14" stop-color="var(--studio-wall)"/>
        <stop offset="0.3" stop-color="var(--curtain-blue)"/>
        <stop offset="0.45" stop-color="var(--skin-warm)"/>
        <stop offset="0.6" stop-color="var(--shirt-teal)"/>
        <stop offset="0.78" stop-color="var(--studio-wall)"/>
        <stop offset="1" stop-color="var(--mat-violet)"/>
      </linearGradient>
    </defs>

    <!-- yellow swoosh on the right of the class photo -->
    <path class="swoosh swoosh--yellow-right" d="M760,0 H820 C800,150 830,330 880,527 H845 C800,360 770,170 760,0 Z" fill="var(--sun-yellow)"/>

    <!-- class photo area -->
    <path class="class-photo" role="img" aria-label="Photo of seniors sitting cross-legged in a bright studio, hands pressed together in prayer pose with eyes closed"
          d="M0,0 H790 C745,140 770,330 815,527 H470 C410,420 250,330 0,318 Z"
          fill="url(#class-photo-tone)"/>

    <!-- teal edge along the photo -->
    <path class="swoosh swoosh--teal-right" d="M790,0 H808 C770,150 795,330 840,527 H815 C770,330 745,140 790,0 Z" fill="var(--lagoon)"/>

    <!-- lower-left swooshes -->
    <path class="swoosh swoosh--yellow-low" d="M0,318 C250,330 410,420 470,527 H505 C430,400 260,305 0,296 Z" fill="var(--sun-yellow)"/>
    <path class="swoosh swoosh--teal-low" d="M0,296 C260,305 430,400 505,527 H520 C450,390 270,290 0,282 Z" fill="var(--lagoon)"/>
  </svg>

  <header class="brand">
    <span class="brand__dot" aria-hidden="true"></span>
    <span class="brand__name">Meadowlark Lane Yoga</span>
    <span class="brand__tagline">Practice Radiant Movement</span>
  </header>

  <section class="instructor">
    <h1 class="instructor__name">Nora<br>Whitfield</h1>
    <p class="instructor__role">Yoga Instructor</p>
    <p class="credentials">MD, Pediatrician<br>RYT-200 RCYT</p>
    <p class="instructor__note">Certified yoga teacher for adults<br>and children</p>
  </section>

  <ul class="contact">
    <li class="contact__item">
      <svg class="contact__icon" viewBox="0 0 26 26" aria-hidden="true">
        <circle cx="13" cy="13" r="13" fill="var(--lagoon)"/>
        <path d="M9,7.5 l2.2,-0.5 1.3,3 -1.5,1.2 c0.7,1.5 1.8,2.6 3.3,3.3 l1.2,-1.5 3,1.3 -0.5,2.2 c-5.5,0.4 -9.4,-3.5 -9,-9 z" fill="var(--paper)"/>
      </svg>
      <span>601-555-0147</span>
    </li>
    <li class="contact__item">
      <svg class="contact__icon" viewBox="0 0 26 26" aria-hidden="true">
        <circle cx="13" cy="13" r="13" fill="var(--lagoon)"/>
        <rect x="6.5" y="8.5" width="13" height="9" rx="1" fill="var(--paper)"/>
        <path d="M6.8,9 L13,13.5 L19.2,9" fill="none" stroke="var(--lagoon)" stroke-width="1.4"/>
      </svg>
      <span>norawhitfield@example.com</span>
    </li>
  </ul>
</main>
</body>
</html>
```